New Business Card for chocolate Company

I am looking to have business cards for my Chocolate Company Velvet Hollow Sweets.
I hand make all organic, fair trade, vegan, gluten free, allergy friendly chocolate. We are located in Austin Texas and are very Proud to be a locally made good. I have my logo and new sticker design for our boxes but now I need cards. I was thinking either natural craft or white. But I want to have a bit of funk to the cards so someone will hold onto it for a long time.
The important info is
Dana Pelworth
Owner and Chocolatier
Velvet Hollow Sweets
velvethollowsweetsatx.com
velvethollowsweets@brivomail.com
velvethollowsweets on instagram
512.373.4816

Velvet Hollow sweets are Vegan ,Gluten free, organic, fair trade, allergy friendly hand made chocolate.

Target Market(s)

We cater to all ages. Our chocolate is on the higher price scale and is a decadent treat. But we make custom molds for any event kids party's to an elegant wedding.

Industry/Entity Type

Business

Requirements
Must have
• Good design logo and some sort of austin vibe.

```html
<!DOCTYPE html>
<html lang="en">
<head>
<meta charset="utf-8">
<title>Velvet Hollow Sweets — Business Cards</title>
<link rel="stylesheet" href="https://fonts.googleapis.com/css2?family=Noto+Serif:wght@400;700&display=swap">
<style>
  :root {
    --paper: #ffffff;
    --aqua: #b0dfe5;
    --aqua-text: #a3d6de;
    --grey-text: #9b9b9b;
    --rule: #a8a8a8;
    --ink: #1c1a19;
    --seal-ring: #4a3a30;
    --shadow: rgba(0, 0, 0, 0.28);
  }
  * { box-sizing: border-box; margin: 0; padding: 0; }
  html, body {
    width: 1200px; height: 1198px; overflow: hidden;
    background: var(--paper);
    font-family: "Noto Serif", Georgia, serif;
  }
  .stage { position: relative; width: 1200px; height: 1198px; }

  .card { position: absolute; box-shadow: 2px 3px 5px var(--shadow); }

  /* Back card */
  .card-back {
    left: 616px; top: 398px; width: 378px; height: 574px;
    background: var(--aqua);
  }
  .seal {
    position: absolute; left: 96px; top: 200px; width: 182px; height: 182px;
    border-radius: 50%; background: #fbfaf7;
    border: 5px solid var(--seal-ring);
    display: flex; align-items: center; justify-content: center; text-align: center;
  }
  .seal-name {
    font-weight: 700; font-size: 22px; line-height: 1.15; color: var(--ink);
    text-transform: uppercase; width: 130px;
  }
  .back-links {
    position: absolute; left: 0; right: 0; top: 511px; text-align: center;
    font-size: 12px; line-height: 18px; color: var(--ink); font-weight: 700;
  }

  /* Front card */
  .card-front {
    left: 266px; top: 224px; width: 370px; height: 654px;
    background: var(--paper);
  }
  .ribbon { position: absolute; left: 129px; top: 0; width: 143px; height: 286px; }
  .logo-tile {
    position: absolute; left: 141px; top: 65px; width: 121px; height: 145px;
    background: var(--paper);
    display: flex; align-items: center; justify-content: center; text-align: center;
  }
  .logo-name {
    font-weight: 700; font-size: 19px; line-height: 1.2; color: var(--ink);
    text-transform: uppercase;
  }
  .name-block {
    position: absolute; left: 44px; width: 312px; top: 305px; height: 95px;
    border-top: 1px dashed var(--rule); border-bottom: 1px dashed var(--rule);
    text-align: center;
  }
  .person-name {
    margin-top: 16px; font-size: 30px; letter-spacing: 1px;
    color: var(--aqua-text); text-transform: uppercase; font-weight: 400;
  }
  .person-role { margin-top: 4px; font-size: 15px; color: var(--grey-text); }
  .contact {
    position: absolute; left: 0; right: 0; top: 464px; text-align: center;
    font-size: 12.5px; line-height: 16.5px; color: var(--grey-text);
  }
  .divider-ornament {
    position: absolute; left: 76px; top: 561px; width: 218px; height: 12px;
    background: linear-gradient(to right, #e4e4e4, #c8c8c8 50%, #e4e4e4);
    border-radius: 6px;
  }
  .tagline {
    position: absolute; left: 30px; right: 30px; top: 598px; text-align: center;
    font-size: 12.5px; line-height: 16px; color: var(--aqua-text);
  }
</style>
</head>
<body>
<main class="stage">

  <section class="card card-back" aria-label="Card back">
    <div class="seal"><span class="seal-name">Velvet Hollow Sweets</span></div>
    <p class="back-links">
      www.velvethollowsweetsatx.com<br>
      www.friendwall.com/VelvetHollowSweets
    </p>
  </section>

  <section class="card card-front" aria-label="Card front">
    <svg class="ribbon" viewBox="0 0 143 286" aria-hidden="true">
      <polygon points="0,0 143,0 143,286 71.5,254 0,286" fill="var(--aqua)"/>
    </svg>
    <div class="logo-tile"><span class="logo-name">Velvet Hollow Sweets</span></div>

    <div class="name-block">
      <h1 class="person-name">Dana Pelworth</h1>
      <p class="person-role">Owner and Chocolatier</p>
    </div>

    <p class="contact">
      Velvet Hollow Sweets<br>
      www.velvethollowsweetsatx.com<br>
      velvethollowsweets@brivomail.com<br>
      phone:512.373.4816
    </p>

    <div class="divider-ornament" role="img" aria-label="Decorative scroll divider with a small flourish at its centre"></div>

    <p class="tagline">
      Velvet Hollow Sweets are vegan ,gluten free, organic,<br>
      fair trade, allergy friendly hand made chocolate.
    </p>
  </section>

</main>
</body>
</html>
```